Wohnhof am Weiher - Zeitungsinserat für den Verkauf von Eigentumswohnungen

Wir brauchen ein Zeitungsinserat in zwei Formaten. Einmal 296 Breite x 440 Höhe mm und einmal 296 Breite x 220 mm Höhe.
Als Basis dient der sehr grobe Entwurf im Powerpoint (Entwurf.pptx).
Auf dem Entwurf fehlen noch die Kontaktangeben:
Brunnhofer Liegenschaften AG
Seematteweg 14
4387 Tannried
079 462 37 58
rbrunnhofer@tessin-ostwald.ch

Zudem muss noch der Link auf die Webseite aufgeführt werden.
www.wohnhof-am-weiher.ch

Zudem fehlt noch der Text:
Fordern Sie noch heute die Verkaufsunterlagen gedruckt oder per Email an. Schreiben Sie uns einfach eine Chatpost mit Ihrer Adresse.

Ich habe noch Files von den Innenvisualisierungen, den Aussenvisualisierungen sowie unser Logo hinzugefügt. Zudem habe ich Ihnen die Verkaufsbrochure angefügt. Sie können die Daten vom Entwurf gerne ergänzen wenn Ihnen etwas gefällt. Schön wäre es, wenn Sie den Stil ähnlich machen würden wie die Brochure.

Target Market(s)

Famillien, Paare und Rentner

Font styles to use
Serif

Colors

Designer to choose colors to be used in the design.

Requirements
Must have
• Tolles Design das sofort anspricht!

```html
<!DOCTYPE html>
<html lang="de">
<head>
<meta charset="utf-8">
<title>Wohnhof am Weiher – Inserat</title>
<link href="https://fonts.googleapis.com/css2?family=Poppins:wght@300;400;500;600;700&display=swap" rel="stylesheet">
<style>
:root{
  --blue:#2b8fd6;
  --ink:#2f3236;
  --muted:#4a4d52;
  --row:#efefef;
  --line:#dcdcdc;
  --stage:#8f96a3;
  --white:#ffffff;
}
*{box-sizing:border-box;margin:0;padding:0}
html,body{width:1200px;height:2400px;overflow:hidden}
body{background:var(--stage);font-family:'Poppins',sans-serif;color:var(--ink);position:relative}

.ad{position:absolute;left:127px;width:933px;background:var(--white);overflow:hidden}
.ad-tall{top:110px;height:1387px}
.ad-wide{top:1597px;height:693px}

/* tall format */
.hero{position:absolute;left:0;top:0;width:933px;height:429px;
  background:linear-gradient(180deg,#e6ecf2 0%,#dfe5ea 45%,#c9ccc9 62%,#9aa08f 75%,#6f8a52 88%,#567a3a 100%)}
.hero-title{position:absolute;left:48px;top:44px}
.hero-title h1{font-weight:700;font-size:39px;line-height:44px;color:var(--blue)}
.hero-title p{font-size:21px;line-height:26px;color:var(--ink);font-weight:400}
.brand-box{position:absolute;left:598px;top:0;width:335px;height:221px;background:var(--blue);
  display:flex;align-items:center;justify-content:center;text-align:center}
.brand-name{color:var(--white);font-weight:600;font-size:27px;line-height:32px;letter-spacing:1px}

.house{position:absolute;left:48px;width:837px;height:212px;background:var(--row)}
.house-tab{position:absolute;left:0;top:0;width:62px;height:100%;background:var(--blue);
  display:flex;align-items:center;justify-content:center}
.house-tab span{transform:rotate(-90deg);white-space:nowrap;color:var(--white);font-weight:700;font-size:24px}
.house-rows{position:absolute;left:62px;top:10px;right:0}
.unit{display:grid;grid-template-columns:154px 135px 96px 224px 1fr;height:38px;padding-left:37px;font-size:13px;line-height:14px;color:var(--muted)}
.unit span{border-right:1px solid var(--line);padding-right:8px}
.unit span:last-child{border-right:0;padding-left:16px}
.unit span:nth-child(4){padding-left:0}

.perk{position:absolute;width:400px}
.perk .tick{position:absolute;left:-47px;top:-2px;width:34px;height:34px}
.perk h3{font-weight:600;font-size:18px;line-height:22px;color:var(--ink)}
.perk p{font-size:13.5px;line-height:16px;color:var(--muted);margin-top:10px;font-weight:400}

/* wide format */
.banner{position:absolute;left:0;top:0;width:933px;height:112px;background:var(--blue)}
.banner h1{position:absolute;left:21px;top:18px;font-weight:700;font-size:41px;line-height:44px;color:var(--white)}
.banner p{position:absolute;left:21px;top:63px;font-size:22px;line-height:26px;color:var(--white)}
.banner .brand-name{position:absolute;right:22px;top:30px;font-size:18px;line-height:22px;text-align:center}
.col{position:absolute;top:117px;width:311px;height:379px}
.col-photo{height:174px;position:relative}
.photo-a{background:linear-gradient(160deg,#f2f1ef,#d9d4cc 55%,#b69d7c)}
.photo-b{background:linear-gradient(180deg,#d8e3ec,#cfd4d6 50%,#8aa06a 80%,#5f7f3d)}
.photo-c{background:linear-gradient(160deg,#f4f4f3,#e2ddd6 60%,#c7b9a5)}
.col-label{position:absolute;left:0;bottom:0;width:137px;height:33px;background:var(--blue);color:var(--white);
  font-weight:600;font-size:15px;line-height:33px;padding-left:20px}
.col-rows{background:var(--row);height:205px;padding-top:9px}
.mini{display:grid;grid-template-columns:52px 48px 42px 93px 1fr;height:38px;padding-left:20px;font-size:8.5px;line-height:10.5px;color:var(--muted)}
.mini span{border-right:1px solid var(--line);padding-right:4px}
.mini span:nth-child(n+2){padding-left:0}
.mini span:last-child{border-right:0;padding-left:4px}
.col-rows .mini span:nth-child(2),.col-rows .mini span:nth-child(3),.col-rows .mini span:nth-child(4){padding-left:0}

.perk-s{position:absolute;width:260px}
.perk-s .tick{position:absolute;left:-34px;top:-3px;width:25px;height:25px}
.perk-s h3{font-weight:500;font-size:13.5px;line-height:16px;color:var(--ink)}
.perk-s p{font-size:9.5px;line-height:11.5px;color:var(--muted);margin-top:9px}
</style>
</head>
<body>

<svg width="0" height="0" style="position:absolute">
  <defs>
    <symbol id="tick" viewBox="0 0 34 34">
      <circle cx="17" cy="17" r="15.5" fill="none" stroke="#2b8fd6" stroke-width="2"/>
      <path d="M10.5 17.5l4.5 4.5 8.5-9" fill="none" stroke="#2b8fd6" stroke-width="2" stroke-linecap="round" stroke-linejoin="round"/>
    </symbol>
  </defs>
</svg>

<!-- Hochformat -->
<section class="ad ad-tall">
  <div class="hero" role="img" aria-label="Aussenvisualisierung der Wohnanlage mit Wiese und Weg"></div>
  <div class="hero-title">
    <h1>Wohnhof am Weiher</h1>
    <p>Hochwertige und moderne Eigentumswohnungen</p>
  </div>
  <div class="brand-box"><div class="brand-name">BRUNNHOFER<br>LIEGENSCHAFTEN AG</div></div>

  <div class="house" style="top:336px">
    <div class="house-tab"><span>Haus A</span></div>
    <div class="house-rows">
      <div class="unit"><span>Attika</span><span>4.5 Zimmer</span><span>108m²</span><span>105m² Sonnenterrasse</span><span>945’000 CHF</span></div>
      <div class="unit"><span>Oberges choss</span><span>3.5 Zimmer</span><span>82m²</span><span>16m² Balkon</span><span>754’800 CHF</span></div>
      <div class="unit"><span>Oberges choss</span><span>4.5 Zimmer</span><span>102m²</span><span>33m² Balkon</span><span>640’000 CHF</span></div>
      <div class="unit"><span>Endgesc hoss</span><span>3.5 Zimmer</span><span>81m²</span><span>16m² gedeckter Sitzplatz &amp; eigener Garten</span><span>657’000 CHF</span></div>
      <div class="unit"><span>Endgesc hoss</span><span>4.5 Zimmer</span><span>102m²</span><span>33m² gedeckter Sitzplatz &amp; eigener Garten</span><span>765’000 CHF</span></div>
    </div>
  </div>

  <div class="house" style="top:555px">
    <div class="house-tab"><span>Haus B</span></div>
    <div class="house-rows">
      <div class="unit"><span>Attika</span><span>4.5 Zimmer</span><span>109m²</span><span>107m² Sonnenterrasse</span><span>965’000 CHF</span></div>
      <div class="unit"><span>Oberges choss</span><span>2.5 Zimmer</span><span>69m²</span><span>14m² Balkon</span><span>550’00 CHF</span></div>
      <div class="unit"><span>Oberges choss</span><span>4.5 Zimmer</span><span>117m²</span><span>42m² Balkon</span><span>887’500 CHF</span></div>
      <div class="unit"><span>Endgesc hoss</span><span>2.5 Zimmer</span><span>69m²</span><span>14m² gedeckter Sitzplatz &amp; eigener Garten</span><span>560’000 CHF</span></div>
      <div class="unit"><span>Endgesc hoss</span><span>4.5 Zimmer</span><span>117m²</span><span>42m² gedeckter Sitzplatz &amp; eigener Garten</span><span>889’000 CHF</span></div>
    </div>
  </div>

  <div class="house" style="top:775px">
    <div class="house-tab"><span>Haus C</span></div>
    <div class="house-rows">
      <div class="unit"><span>Attika</span><span>4.5 Zimmer</span><span>129m²</span><span>132m² Sonnenterrasse</span><span>1’125’000 CHF</span></div>
      <div class="unit"><span>Oberges choss</span><span>5.5 Zimmer</span><span>143m²</span><span>43m² Balkon</span><span>1’058’000 CHF</span></div>
      <div class="unit"><span>Oberges choss</span><span>3.5 Zimmer</span><span>96m²</span><span>23m² Balkon</span><span>730’000 CHF</span></div>
      <div class="unit"><span>Endgesc hoss</span><span>5.5 Zimmer</span><span>143m²</span><span>43m² gedeckter Sitzplatz &amp; eigener Garten</span><span>1’065’000 CHF</span></div>
      <div class="unit"><span>Endgesc hoss</span><span>3.5 Zimmer</span><span>96m²</span><span>23m² gedeckter Sitzplatz &amp; eigener Garten</span><span>740’000 CHF</span></div>
    </div>
  </div>

  <div class="perk" style="left:107px;top:1018px;width:360px">
    <svg class="tick"><use href="#tick"/></svg>
    <h3>Bus und Bahn</h3>
    <p>Der Bahnhof von Feldbrugg mit Zugverbindungen nach Riedstadt (20 Minuten) und Morelon ist in wenigen Minuten mit dem Bus zu erreichen.</p>
  </div>
  <div class="perk" style="left:107px;top:1120px;width:360px">
    <svg class="tick"><use href="#tick"/></svg>
    <h3>Riedstadt - Stadt</h3>
    <p>Der nahegelegene Bahnhof in Feldbrugg verfügt über sehr gute Verbindungen nach Riedstadt (20 Minuten), welche durch den Doppelspurausbau in den kommenden Jahren sogar noch weiter verbessert werden.</p>
  </div>
  <div class="perk" style="left:107px;top:1242px;width:370px">
    <svg class="tick"><use href="#tick"/></svg>
    <h3>Autobahn</h3>
    <p>Die Wohnsiedlung ist ideal auch für den Individualverkehr erschlossen. Die Entfernung zur Autobahn J27 beträgt 12km und ist über Eschwil innerhalb von 15 Minuten erreichbar</p>
  </div>
  <div class="perk" style="left:543px;top:1018px;width:345px">
    <svg class="tick"><use href="#tick"/></svg>
    <h3>Einkaufen und weitere<br>Dienstleistungen</h3>
    <p>Durch die Nähe der Gemeindegrenze zwischen Feldbrugg und Tannried liegen die Dorfzentren mit ihren Einkaufsmöglichkeiten (z.B. Talmatt Center Feldbrugg sowie der Altstadt in Feldbrugg) und Dienstleistungsangeboten in max. 2 Minuten Fahrtzeit oder in 10-15 Minuten Gehdistanz.</p>
  </div>
  <div class="perk" style="left:543px;top:1201px;width:350px">
    <svg class="tick"><use href="#tick"/></svg>
    <h3>Erholung im Grünen</h3>
    <p>Tannried erfüllt mit seinen Wäldern, dem eigenen «Hangwald» dem «Felsenkopf», den offenen Feldern, den Wander- und Velorouten und der ländlichen Ruhe alle Voraussetzungen, die ein Naherholungsgebiet begehrt machen.</p>
  </div>
</section>

<!-- Querformat -->
<section class="ad ad-wide">
  <header class="banner">
    <h1>Wohnhof am Weiher</h1>
    <p>Hochwertige und moderne Eigentumswohnungen</p>
    <div class="brand-name">BRUNNHOFER<br>LIEGENSCHAFTEN AG</div>
  </header>

  <div class="col" style="left:0">
    <div class="col-photo photo-a" role="img" aria-label="Innenvisualisierung Wohn- und Essbereich"><div class="col-label">Haus A</div></div>
    <div class="col-rows">
      <div class="mini"><span>Attika</span><span>4.5 Zimmer</span><span>108m²</span><span>105m² Sonnenterrasse</span><span>945’000 CHF</span></div>
      <div class="mini"><span>Oberges choss</span><span>3.5 Zimmer</span><span>82m²</span><span>16m² Balkon</span><span>754’800 CHF</span></div>
      <div class="mini"><span>Oberges choss</span><span>4.5 Zimmer</span><span>102m²</span><span>33m² Balkon</span><span>640’000 CHF</span></div>
      <div class="mini"><span>Endgesc hoss</span><span>3.5 Zimmer</span><span>81m²</span><span>16m² gedeckter Sitzplatz &amp; eigener Garten</span><span>657’000 CHF</span></div>
      <div class="mini"><span>Endgesc hoss</span><span>4.5 Zimmer</span><span>102m²</span><span>33m² gedeckter Sitzplatz &amp;eigener Garten</span><span>765’000 CHF</span></div>
    </div>
  </div>

  <div class="col" style="left:311px">
    <div class="col-photo photo-b" role="img" aria-label="Aussenvisualisierung der Wohnanlage"><div class="col-label">Haus B</div></div>
    <div class="col-rows">
      <div class="mini"><span>Attika</span><span>4.5 Zimmer</span><span>109m²</span><span>107m² Sonnenterrasse</span><span>965’000 CHF</span></div>
      <div class="mini"><span>Oberges choss</span><span>2.5 Zimmer</span><span>69m²</span><span>14m² Balkon</span><span>550’000 CHF</span></div>
      <div class="mini"><span>Oberges choss</span><span>4.5 Zimmer</span><span>117m²</span><span>42m² Balkon</span><span>877’500 CHF</span></div>
      <div class="mini"><span>Endgesc hoss</span><span>2.5 Zimmer</span><span>69m²</span><span>14m² gedeckter Sitzplatz &amp; eigener Garten</span><span>560’000 CHF</span></div>
      <div class="mini"><span>Endgesc hoss</span><span>4.5 Zimmer</span><span>117m²</span><span>42m² gedeckter Sitzplatz &amp;eigener Garten</span><span>889’000 CHF</span></div>
    </div>
  </div>

  <div class="col" style="left:622px">
    <div class="col-photo photo-c" role="img" aria-label="Innenvisualisierung Küche und Essbereich"><div class="col-label">Haus C</div></div>
    <div class="col-rows">
      <div class="mini"><span>Attika</span><span>4.5 Zimmer</span><span>129m²</span><span>132m² Sonnenterrasse</span><span>1’125’000 CHF</span></div>
      <div class="mini"><span>Oberges choss</span><span>5.5 Zimmer</span><span>143m²</span><span>43m² Balkon</span><span>1’058’800 CHF</span></div>
      <div class="mini"><span>Oberges choss</span><span>3.5 Zimmer</span><span>96m²</span><span>23m² Balkon</span><span>730’000 CHF</span></div>
      <div class="mini"><span>Endgesc hoss</span><span>5.5 Zimmer</span><span>143m²</span><span>43m² gedeckter Sitzplatz &amp; eigener Garten</span><span>1’065’000 CHF</span></div>
      <div class="mini"><span>Endgesc hoss</span><span>3.5 Zimmer</span><span>96m²</span><span>23m² gedeckter Sitzplatz &amp;eigener Garten</span><span>740’000 CHF</span></div>
    </div>
  </div>

  <div class="perk-s" style="left:54px;top:516px;width:240px">
    <svg class="tick"><use href="#tick"/></svg>
    <h3>Bus und Bahn</h3>
    <p>Der Bahnhof von Feldbrugg mit Zugverbindungen nach Riedstadt (20 Minuten) und Morelon ist in wenigen Minuten mit dem Bus zu erreichen.</p>
  </div>
  <div class="perk-s" style="left:54px;top:592px;width:245px">
    <svg class="tick"><use href="#tick"/></svg>
    <h3>Riedstadt - Stadt</h3>
    <p>Der nahegelegene Bahnhof in Feldbrugg verfügt über sehr gute Verbindungen nach Riedstadt (20 Minuten), welche durch den Doppelspurausbau in den kommenden Jahren sogar noch weiter verbessert werden.</p>
  </div>
  <div class="perk-s" style="left:343px;top:516px;width:270px">
    <svg class="tick"><use href="#tick"/></svg>
    <h3>Autobahn</h3>
    <p>Die Wohnsiedlung ist ideal auch für den Individualverkehr erschlossen. Die Entfernung zur Autobahn J27 beträgt 12km und ist über Eschwil innerhalb von 15 Minuten erreichbar</p>
  </div>
  <div class="perk-s" style="left:343px;top:589px;width:265px">
    <svg class="tick"><use href="#tick"/></svg>
    <h3>Erholung im Grünen</h3>
    <p>Tannried erfüllt mit seinen Wäldern, dem eigenen «Hangwald» dem «Felsenkopf», den offenen Feldern, den Wander- und Velorouten und der ländlichen Ruhe alle Voraussetzungen, die ein Naherholungsgebiet begehrt machen.</p>
  </div>
  <div class="perk-s" style="left:663px;top:516px;width:240px">
    <svg class="tick"><use href="#tick"/></svg>
    <h3>Einkaufen und weitere<br>Dienstleistungen</h3>
    <p>Durch die Nähe der Gemeindegrenze zwischen Feldbrugg und Tannried liegen die Dorfzentren mit ihren Einkaufsmöglichkeiten (z.B. Talmatt Center Feldbrugg sowie der Altstadt in Feldbrugg) und Dienstleistungsangeboten in max. 2 Minuten Fahrtzeit oder in 10-15 Minuten Gehdistanz.</p>
  </div>
</section>

</body>
</html>
```